Harborline Wellness Partners

Please design a business card that is colorful but at the same time easy to read. We are based out on Miami Florida. We are a small start up healthcare company that has been in operation for 1 year. Our clients are Hospitals, Insurance companies, and Manage Care health companies. We are growing quickly and lead the niche we are in. Please make the card 2 sided on the front will be the typical info. Logo, Company Name, Persons Name, Title, Cell #, Office #, Fax#, email, website. No address. On the back we will list 5 services that we do. For example Care Transitions, Case management, Risk assessment, Utilization Review.
Target Market(s)
CEO's and COO's of hospitals and healthcare companies.
Industry/Entity Type
Healthcare

```html
<!DOCTYPE html>
<html lang="en">
<head>
<meta charset="utf-8">
<title>Harborline Wellness Partners — Business Card</title>
<link rel="stylesheet" href="https://fonts.googleapis.com/css2?family=Questrial&family=Exo+2:wght@500&display=swap">
<style>
  :root {
    --bg: #8c8c8c;
    --paper: #ffffff;
    --navy: #2b3990;
    --blue: #0f75bc;
    --ink: #333333;
    --rule: #9a9a9a;
    --tab-1: #2b3990;
    --tab-2: #28469c;
    --tab-3: #1c5aa8;
    --tab-4: #1b75bc;
    --tab-5: #27aae1;
    --tab-6: #ece93a;
    --tab-7: #ed1c24;
    --tab-8: #1fa64a;
    --tab-9: #2bb04f;
    --tab-10: #8dc63f;
  }
  * { margin: 0; padding: 0; box-sizing: border-box; }
  html, body { width: 1200px; height: 1000px; overflow: hidden; }
  body {
    position: relative;
    background: var(--bg);
    font-family: "Questrial", sans-serif;
  }
  .card {
    position: absolute;
    width: 544px;
    height: 319px;
    background: var(--paper);
    border: 1px solid #6e6e6e;
    overflow: hidden;
  }
  /* Front */
  .card-front { left: 38px; top: 38px; }
  .brand {
    position: absolute;
    left: 130px; top: 22px;
    display: flex; align-items: center; gap: 22px;
  }
  .brand-dot {
    width: 90px; height: 90px; border-radius: 50%;
    background: var(--blue);
    flex: none;
  }
  .brand-name {
    font-size: 29px; line-height: 42px;
    color: var(--navy);
  }
  .person { position: absolute; left: 54px; top: 200px; text-align: center; }
  .person-name { font-size: 27px; color: var(--navy); letter-spacing: 0.5px; }
  .person-title { font-size: 15px; color: var(--ink); margin-top: 2px; }
  .contact {
    position: absolute; left: 280px; top: 172px;
    border-left: 1px solid var(--rule);
    padding-left: 9px;
    font-size: 15px; line-height: 19px; color: var(--ink);
    list-style: none;
  }
  .contact-row { display: flex; align-items: center; gap: 5px; }
  .contact-row svg { width: 11px; height: 11px; flex: none; }
  .tabs {
    position: absolute; left: 0; right: 0; bottom: 0;
    display: flex; gap: 3px; height: 16px;
  }
  .tab { flex: 1; border-radius: 4px 4px 0 0; }
  /* Back */
  .card-back { display: flex; }
  .card-back.back-a { left: 620px; top: 178px; }
  .card-back.back-b { left: 620px; top: 613px; }
  .services {
    background: linear-gradient(180deg, var(--navy) 0%, var(--blue) 100%);
    padding: 44px 0 0 51px;
    font-family: "Exo 2", sans-serif;
    font-weight: 500;
    color: #ffffff;
    font-size: 23px;
    letter-spacing: 0.6px;
    list-style: none;
  }
  .services li { line-height: 46px; white-space: nowrap; }
  .back-a .services { width: 315px; }
  .back-b .services { width: 313px; padding-left: 32px; order: 2; }
  .back-mark {
    flex: 1;
    display: flex; align-items: center; justify-content: center; gap: 12px;
  }
  .back-mark .brand-dot { width: 40px; height: 40px; }
  .back-mark .brand-name { font-size: 22px; line-height: 30px; }
</style>
</head>
<body>

  <section class="card card-front" aria-label="Business card front">
    <div class="brand">
      <span class="brand-dot"></span>
      <div class="brand-name">Harborline<br>Wellness<br>Partners</div>
    </div>

    <div class="person">
      <div class="person-name">Daniel Reyes</div>
      <div class="person-title">Director</div>
    </div>

    <ul class="contact">
      <li class="contact-row">
        <svg viewBox="0 0 12 12"><rect x="3" y="0.5" width="6" height="11" rx="1" fill="var(--navy)"/><rect x="4" y="2" width="4" height="6" fill="#fff"/></svg>
        <span>305.555.0142</span>
      </li>
      <li class="contact-row">
        <svg viewBox="0 0 12 12"><path d="M3 1 L5 4 L4 5 Q5 7.5 7 8 L8 7 L11 9 L10 11 Q3 10 1 2 Z" fill="var(--tab-8)"/></svg>
        <span>305.555.0143</span>
      </li>
      <li class="contact-row">
        <svg viewBox="0 0 12 12"><rect x="3" y="0.5" width="6" height="4" fill="var(--tab-7)"/><rect x="1" y="4" width="10" height="7" rx="1" fill="var(--tab-7)"/><rect x="3" y="6" width="6" height="1.5" fill="#fff"/></svg>
        <span>305.555.0144</span>
      </li>
      <li class="contact-row">
        <svg viewBox="0 0 12 12"><rect x="0.5" y="2" width="11" height="8" rx="1" fill="var(--navy)"/><path d="M1 2.5 L6 7 L11 2.5" stroke="#fff" stroke-width="1" fill="none"/></svg>
        <span>dreyes@harborlinewp.com</span>
      </li>
      <li class="contact-row">
        <svg viewBox="0 0 12 12"><circle cx="6" cy="6" r="5" fill="var(--tab-5)"/><path d="M1 6 H11 M6 1 V11 M3 2.5 Q6 4 9 2.5 M3 9.5 Q6 8 9 9.5" stroke="#fff" stroke-width="0.8" fill="none"/></svg>
        <span>www.harborlinewp.com</span>
      </li>
    </ul>

    <div class="tabs">
      <span class="tab" style="background:var(--tab-1)"></span>
      <span class="tab" style="background:var(--tab-2)"></span>
      <span class="tab" style="background:var(--tab-3)"></span>
      <span class="tab" style="background:var(--tab-4)"></span>
      <span class="tab" style="background:var(--tab-5)"></span>
      <span class="tab" style="background:var(--tab-6)"></span>
      <span class="tab" style="background:var(--tab-7)"></span>
      <span class="tab" style="background:var(--tab-8)"></span>
      <span class="tab" style="background:var(--tab-9)"></span>
      <span class="tab" style="background:var(--tab-10)"></span>
    </div>
  </section>

  <section class="card card-back back-a" aria-label="Business card back, services left">
    <ul class="services">
      <li>Care Transitions</li>
      <li>Case Management</li>
      <li>Risk Assessment</li>
      <li>Utilization Review</li>
      <li>Discharge Planning</li>
    </ul>
    <div class="back-mark">
      <span class="brand-dot"></span>
      <div class="brand-name">Harborline<br>Wellness<br>Partners</div>
    </div>
  </section>

  <section class="card card-back back-b" aria-label="Business card back, services right">
    <ul class="services">
      <li>Care Transitions</li>
      <li>Case Management</li>
      <li>Risk Assessment</li>
      <li>Utilization Review</li>
      <li>Discharge Planning</li>
    </ul>
    <div class="back-mark">
      <span class="brand-dot"></span>
      <div class="brand-name">Harborline<br>Wellness<br>Partners</div>
    </div>
  </section>

</body>
</html>
```